CoverLantern.com website re-design - modern engaging website creation

We have an existing website. Www.CoverLantern.com - the content on the site and our widgets are custom built. But the layout and design of our site we just put there as we built the functionality around it. We want a new, bold, and modern design aimed at getting visitors to run a life insurance quote and ultimately apply. Our demographic is centered around those between the ages of 30-60. So we are looking at a complete site overhaul with better pictures, buttons, and an extremely modern design.

Target Market(s)

30-50 year olds

Industry/Entity Type

Life insurance

Coding

Coded - Design and coding required

Number of Pages Required

5+ page

Font styles to use
Other font styles liked:
• Rubik

Colors
0054AA
0677BA
7BADD7
CADEEF
E8F1F8
00AB8E
00BBA5
67D7C9
C6EFE9
E9F9F6
59FF00
82FF00
B8FF75
E3FFCB
F4FFEA

Requirements
Must have
• Matching color schemes from existing website. We have custom widgets on our site now and those must be . White space is important to make it simple for the user to navigate
Nice to have
• Same content - different more modern design
Should not have
• Colors outside of our current color scheme. Should NOT be too similar to our existing site.

```html
<!DOCTYPE html>
<html lang="en">
<head>
<meta charset="UTF-8">
<title>CoverLantern — Life Insurance Made Simple</title>
<link href="https://fonts.googleapis.com/css2?family=Poppins:wght@400;500;600;700;800&family=Roboto+Condensed:wght@400;700&display=swap" rel="stylesheet">
<style>
:root{
  --blue:#0054AA;
  --blue-mid:#0677BA;
  --blue-soft:#7BADD7;
  --blue-pale:#CADEEF;
  --green:#84C93F;
  --green-dark:#6FB52C;
  --ink:#111111;
  --grey:#555555;
  --line:#E6E6E6;
  --white:#ffffff;
}
*{box-sizing:border-box;margin:0;padding:0}
html,body{width:1200px;height:4315px;overflow:hidden;background:var(--white)}
body{font-family:'Poppins',sans-serif;color:var(--ink)}
.page{position:relative;width:1200px;height:4315px;overflow:hidden}
.abs{position:absolute}
.shape{position:absolute;left:0;width:1200px}
.btn{position:absolute;display:flex;align-items:center;justify-content:center;background:var(--green);color:var(--white);font-weight:700;font-size:11px;letter-spacing:.3px;text-transform:uppercase;border-radius:2px;text-decoration:none}
.btn--blue{background:var(--blue)}
.btn--soft{background:#6C8FD6}
.accent{color:var(--green)}
.accent-blue{color:var(--blue)}

/* header */
.logo{position:absolute;font-weight:400;font-size:30px;color:var(--white);letter-spacing:-.5px}
.logo--footer{font-size:24px}
.nav{position:absolute;left:323px;top:68px;display:flex;gap:28px}
.nav a{color:var(--white);font-size:10px;font-weight:600;text-decoration:none;text-transform:uppercase}

/* hero */
.hero-title{left:100px;top:222px;font-size:40px;font-weight:800;line-height:50px;color:var(--white);text-transform:uppercase}
.hero-sub{left:100px;top:392px;font-size:14px;color:var(--white);line-height:20px}
.hero-sub b{color:var(--green);font-weight:700}
.art{position:absolute}

.quote-card{position:absolute;left:810px;top:208px;width:290px;height:327px;background:var(--white);box-shadow:0 8px 30px rgba(0,0,0,.12)}
.quote-card__head{height:66px;background:#6D9FD9;color:var(--white);font-weight:700;font-size:16px;display:flex;align-items:center;justify-content:center}
.steps{position:relative;margin:34px 22px 0;height:30px}
.steps__line{position:absolute;left:14px;right:14px;top:6px;height:2px;background:#D8D8D8}
.steps__dot{position:absolute;top:0;width:14px;height:14px;border-radius:50%;background:#D8D8D8}
.steps__label{position:absolute;top:18px;font-size:11px;font-weight:600}
.quote-card__q{text-align:center;font-size:12px;font-weight:600;margin-top:18px}
.select{margin:22px 22px 0;height:36px;border:1px solid #D5D5D5;border-radius:2px;font-size:9px;color:#999;display:flex;align-items:center;justify-content:space-between;padding:0 20px}
.quote-card .btn{left:22px;top:262px;width:246px;height:38px}

/* carrier row */
.carriers{position:absolute;left:100px;top:755px;width:1000px;height:138px;border-top:1px solid var(--line);border-bottom:1px solid var(--line);display:flex;align-items:center;justify-content:space-between;padding:0 10px}
.carriers span{font-weight:700;font-size:20px;color:#333}

/* sections */
.h2{position:absolute;font-size:28px;font-weight:800;text-transform:uppercase;line-height:34px}
.h2--light{color:var(--white)}
.lead{position:absolute;font-size:12px;color:var(--grey);line-height:22px}
.ticks{position:absolute;list-style:none}
.ticks li{position:relative;padding-left:24px;font-size:14px;line-height:21px;margin-bottom:22px}
.ticks li::before{content:"";position:absolute;left:0;top:4px;width:12px;height:12px;border-radius:50%;background:var(--green)}
.ticks li::after{content:"";position:absolute;left:4px;top:6px;width:3px;height:5px;border:solid var(--white);border-width:0 2px 2px 0;transform:rotate(45deg)}
.ticks--light li{color:var(--white)}
.ticks--dark li{color:#444}
.ticks--blue li::before{background:var(--blue)}

.rate{position:absolute;height:122px;background:var(--white);border-radius:61px;box-shadow:0 10px 28px rgba(0,0,0,.2);display:flex;align-items:center}
.rate__name{width:150px;text-align:center;font-size:24px;font-weight:600;color:#222}
.rate__info{font-family:'Roboto Condensed',sans-serif;font-size:12px;color:#555;line-height:20px;padding-left:16px;border-left:1px solid #ddd;text-align:center}
.rate__price{font-family:'Poppins',sans-serif;font-size:32px;font-weight:800;color:#111;line-height:36px}
.rate__price small{font-size:12px;font-weight:600}

.footer-col{position:absolute;top:4040px;color:var(--white)}
.footer-col h4{font-size:15px;font-weight:700;margin-bottom:16px}
.footer-col li{list-style:none;font-size:12px;line-height:27px;position:relative}
.footer-col .dotlist li{padding-left:18px}
.footer-col .dotlist li::before{content:"";position:absolute;left:0;top:10px;width:8px;height:8px;border-radius:50%;background:var(--white)}
.footer-col .iconlist li{padding-left:22px}
.footer-col .iconlist li::before{content:"";position:absolute;left:2px;top:10px;width:8px;height:8px;border-radius:50%;background:var(--green)}
.footer-col .iconlist li.plain::before{display:none}
.social{position:absolute;left:100px;top:4157px;display:flex;gap:22px}
.social span{width:24px;height:24px;border-radius:50%;background:var(--green)}
.footer-rule{position:absolute;left:100px;top:4245px;width:1000px;height:1px;background:rgba(255,255,255,.35)}
.copyright{position:absolute;left:0;top:4272px;width:1200px;text-align:center;font-size:10px;color:var(--white)}
</style>
</head>
<body>
<div class="page">

  <!-- HERO BACKGROUND -->
  <svg class="shape" style="top:0" width="1200" height="700" viewBox="0 0 1200 700">
    <ellipse cx="1015" cy="395" rx="170" ry="265" fill="#84C93F"/>
    <path d="M0 0H1200V150C1100 340 820 560 430 625C260 652 110 660 0 662Z" fill="#0054AA"/>
    <path d="M0 662C180 680 420 660 600 600C420 640 200 670 0 686Z" fill="#84C93F"/>
    <path d="M1200 150L1200 175C1160 190 1130 205 1110 220C1140 195 1170 170 1200 150Z" fill="#84C93F"/>
  </svg>

  <div class="logo" style="left:100px;top:58px">CoverLantern</div>
  <nav class="nav">
    <a href="#">Free Quote</a><a href="#">No Exam</a><a href="#">Articles</a><a href="#">FAQ's</a><a href="#">About</a><a href="#">Contact</a>
  </nav>
  <a class="btn" href="#" style="left:783px;top:57px;width:152px;height:38px;font-size:9px">Continue Application</a>
  <a class="btn btn--soft" href="#" style="left:948px;top:57px;width:152px;height:38px;font-size:9px">Existing Client Login</a>

  <h1 class="abs hero-title"><span class="accent">CoverLantern</span> makes<br>you the insurance<br>agent</h1>
  <p class="abs hero-sub">Best Rates For Term Life Insurance Form<br><b>Americas Top Rated</b> Carriers</p>
  <a class="btn" href="#" style="left:100px;top:474px;width:152px;height:38px">Get Tour Quote</a>

  <div class="art" role="img" aria-label="Illustrated robot assistant mascot holding a clipboard" style="left:540px;top:258px;width:200px;height:430px;border-radius:90px;background:linear-gradient(180deg,#2A6FD0,#123F8C)"></div>

  <div class="quote-card">
    <div class="quote-card__head">GET A QUOTE</div>
    <div class="steps">
      <div class="steps__line"></div>
      <div class="steps__dot" style="left:10px;background:var(--green)"></div>
      <div class="steps__dot" style="left:124px"></div>
      <div class="steps__dot" style="left:234px"></div>
      <div class="steps__label" style="left:8px">Step 1</div>
      <div class="steps__label" style="left:114px">Step 2</div>
      <div class="steps__label" style="left:224px">Step 3</div>
    </div>
    <p class="quote-card__q">What state do you live in ?</p>
    <div class="select">Pick your state
      <svg width="10" height="6" viewBox="0 0 10 6"><path d="M1 1l4 4 4-4" fill="none" stroke="#888" stroke-width="1.2"/></svg>
    </div>
    <a class="btn btn--blue" href="#">Proceed to next</a>
  </div>

  <!-- CARRIERS -->
  <div class="carriers">
    <span>Northgate</span><span>Keystone Mutual</span><span>HarborLife</span><span>Shieldwell</span><span>Atlas</span><span>Crestmark</span>
  </div>

  <!-- LIFE INSURANCE ONLINE -->
  <svg class="shape" style="top:1050px" width="1200" height="380" viewBox="0 0 1200 380">
    <path d="M0 170L84 30L8 160L0 190Z" fill="#84C93F"/>
    <path d="M1090 370L1200 230V260L1110 370Z" fill="#84C93F"/>
  </svg>
  <h2 class="h2" style="left:132px;top:1068px">Life insurance <span class="accent">online</span></h2>
  <p class="lead" style="left:133px;top:1114px">Compare quotes from America's top insurance carriers<br>Pick your policy and apply in minutes</p>
  <a class="btn" href="#" style="left:133px;top:1178px;width:162px;height:42px">Get Your Quote Now</a>
  <div class="art" role="img" aria-label="Photo of a smiling couple looking at a laptop together" style="left:578px;top:925px;width:475px;height:460px;border-radius:46% 54% 40% 60% / 48% 42% 58% 52%;background:linear-gradient(135deg,#C9A98A,#6E5443)"></div>

  <!-- COMPARE AND SAVE -->
  <svg class="shape" style="top:1420px" width="1200" height="680" viewBox="0 0 1200 680">
    <path d="M0 0H1200V500C1000 590 700 660 300 665C180 667 80 667 0 668Z" fill="#0054AA"/>
  </svg>
  <h2 class="h2 h2--light" style="left:132px;top:1588px">Compare and <span class="accent">save</span></h2>
  <ul class="ticks ticks--light" style="left:132px;top:1638px;width:400px">
    <li>Get Quotes without having to enter your contact information.</li>
    <li>Decide what's best for you without having to deal with pushy insurance agents.</li>
    <li>Virtual agent tools are available to help you choose what life insurance policy is best for you and your family.</li>
  </ul>
  <a class="btn" href="#" style="left:132px;top:1857px;width:155px;height:42px">Compare Carriers</a>

  <div class="rate" style="left:648px;top:1502px;width:350px">
    <div class="rate__name">Northgate</div>
    <div class="rate__info">$2,000,000 Death Benefit<br>20 Year Level Term<div class="rate__price">$18<small>.08/MO</small></div></div>
  </div>
  <div class="rate" style="left:610px;top:1670px;width:352px">
    <div class="rate__name">Shieldwell</div>
    <div class="rate__info">$2,000,000 Death Benefit<br>20 Year Level Term<div class="rate__price">$21<small>.17/MO</small></div></div>
  </div>
  <div class="rate" style="left:683px;top:1840px;width:347px">
    <div class="rate__name" style="color:var(--blue-mid)">Atlas</div>
    <div class="rate__info">$2,000,000 Death Benefit<br>20 Year Level Term<div class="rate__price">$23<small>.28/MO</small></div></div>
  </div>

  <!-- MEET LUMI -->
  <svg class="shape" style="top:2120px" width="1200" height="520" viewBox="0 0 1200 520">
    <path d="M0 170L90 0L10 155L0 180Z" fill="#84C93F"/>
    <path d="M1085 520L1148 355L1108 520Z" fill="#84C93F"/>
  </svg>
  <h2 class="h2 accent-blue" style="left:135px;top:2213px">Meet <span class="accent">Lumi</span></h2>
  <ul class="ticks ticks--dark" style="left:135px;top:2263px;width:400px">
    <li>Our Virtual Agent Lumi can help you calculate how much death benefit you need.</li>
    <li>Lumi can help you figure out what type of Life Insurance is right for you and your family.</li>
    <li>Lumi can evaluate your health history and provide you with accurate quotes.</li>
  </ul>
  <a class="btn" href="#" style="left:135px;top:2460px;width:155px;height:42px">Virtual Agent</a>
  <div class="art" role="img" aria-label="Illustrated robot assistant mascot holding a clipboard" style="left:745px;top:2120px;width:230px;height:470px;border-radius:100px;background:linear-gradient(180deg,#2A6FD0,#123F8C)"></div>

  <!-- LIVE AGENT SUPPORT -->
  <svg class="shape" style="top:2640px" width="1200" height="680" viewBox="0 0 1200 680">
    <path d="M0 0H1200V560C1000 620 700 660 300 665C180 667 80 668 0 670Z" fill="#0054AA"/>
  </svg>
  <div class="art" role="img" aria-label="Photo of a smiling customer support agent wearing a headset" style="left:572px;top:2692px;width:535px;height:520px;border-radius:50% 50% 42% 58% / 40% 50% 50% 60%;background:linear-gradient(135deg,#EAF2F8,#9FBBD3)"></div>
  <h2 class="h2 h2--light" style="left:133px;top:2820px">Live agent <span class="accent">support</span></h2>
  <ul class="ticks ticks--light" style="left:133px;top:2870px;width:400px">
    <li>If you need a Live Agent, CoverLantern has you covered.  Our CoverLantern Agents are not paid a commission. So if you have questions our agents have the answers that best suit your needs.</li>
    <li>Call Toll Free: 1-888-555-0142</li>
    <li>Email: info@coverlantern.com</li>
  </ul>
  <a class="btn" href="#" style="left:133px;top:3062px;width:167px;height:42px">Get Help Now</a>

  <!-- APPLY ONLINE -->
  <svg class="shape" style="top:3310px" width="1200" height="470" viewBox="0 0 1200 470">
    <path d="M0 200L90 5L10 180L0 210Z" fill="#84C93F"/>
    <path d="M1080 450L1200 360V380L1095 455Z" fill="#84C93F"/>
  </svg>
  <div class="art" role="img" aria-label="Photo of a smiling woman working on a laptop" style="left:132px;top:3340px;width:462px;height:495px;border-radius:40% 60% 52% 48% / 50% 44% 56% 50%;background:linear-gradient(135deg,#D9B48F,#7A5A44)"></div>
  <h2 class="h2 accent-blue" style="left:710px;top:3502px">Apply <span class="accent">online</span></h2>
  <ul class="ticks ticks--dark ticks--blue" style="left:710px;top:3548px;width:400px">
    <li>Pick your policy and apply online in minutes.</li>
    <li>Secure Online Portal keeps your information safe and secure.</li>
    <li>24/7 access to your policy documents.</li>
  </ul>
  <a class="btn" href="#" style="left:710px;top:3717px;width:155px;height:42px">Portal Login</a>

  <!-- FOOTER -->
  <svg class="shape" style="top:3830px" width="1200" height="485" viewBox="0 0 1200 485">
    <path d="M0 40C300 110 800 110 1200 40V485H0Z" fill="#0054AA"/>
    <path d="M60 30C380 100 820 100 1160 40C820 80 380 85 60 30Z" fill="#84C93F"/>
    <path d="M0 40C300 120 800 130 1200 40V52C800 140 300 130 0 55Z" fill="#84C93F"/>
  </svg>
  <div class="logo logo--footer" style="left:106px;top:4030px">CoverLantern</div>
  <p class="abs" style="left:106px;top:4078px;width:180px;font-size:12px;line-height:20px;color:var(--white)">Sed ut perspiciatis unde omnis iste natus error sit voluptatem accusantiu.</p>
  <div class="social"><span></span><span></span><span></span><span></span></div>

  <div class="footer-col" style="left:325px">
    <h4>Life Insurance Products</h4>
    <ul class="dotlist"><li>10 Year Level Team</li><li>15 Year Level Team</li><li>20 Year Level Team</li><li>30 Year Level Team</li><li>10 Year Level Team</li></ul>
  </div>
  <div class="footer-col" style="left:578px">
    <h4>Tools</h4>
    <ul class="dotlist"><li>Quote Comparison</li><li>Secure Client Portal</li><li>Privacy Policy</li></ul>
  </div>
  <div class="footer-col" style="left:780px">
    <h4>Contact</h4>
    <ul class="iconlist"><li>1-888-555-0142</li><li>info@coverlantern.com</li><li>Monday - Friday</li><li class="plain">9:00 AM - 8:00 PM</li></ul>
  </div>
  <div class="footer-col" style="left:1007px">
    <h4>Quick Links</h4>
    <ul><li>Free Quote</li><li>No Exam</li><li>Articles</li><li>FAQs</li><li>About</li><li>Contact</li></ul>
  </div>
  <div class="footer-rule"></div>
  <p class="copyright">Copyright 2022 CoverLantern. All Rights Reserved</p>

</div>
</body>
</html>
```